Dynamic Business Card for Sports Supplements Company

Hi! I'm looking for an awesome business card to match my existing sports supplement company. I have uploaded my current company logo and screenshot of the front page of my website.

I would like to have something dynamic and interesting and utilize the colors in the website - the reds and purples

The business card should be double sided and focus on a unique eye-catching design on the back and include all the relevant company info.

Most importantly, it should say somewhere: "Sign up on our website for a coupon code."

Target Market(s)

Mostly for women gym goers but it shouldn't be too feminine. It should be in keeping with the website design. It should flow and clearly be connected to it

Industry/Entity Type

Business

Contact Information for Business Card

Lorena K. Vasquez
CEO
LVasquez@Fortivanco.example
www.fortivanco.example
614.275.3081
P.O. Box 48317
Alderton, Ohio 22417

Sign up on our website for a coupon code

Font styles to use
Serif
Sans Serif
Other font styles liked:
• Novecento font family and "Fortivan" is in AR Destine font

Requirements
Must have
• One side should be a bold Fortivan logo design. Even just the symbol itself may be o.k. (see attached file)

```html
<!DOCTYPE html>
<html lang="en">
<head>
<meta charset="utf-8">
<title>Fortivan Business Card</title>
<link href="https://fonts.googleapis.com/css2?family=Mulish:wght@400;600;800&display=swap" rel="stylesheet">
<style>
  :root {
    --purple: #5e4580;
    --red: #e3222c;
    --white: #ffffff;
    --ink: #1e1e24;
    --backdrop: #5f686d;
  }
  * { box-sizing: border-box; margin: 0; padding: 0; }
  html, body { width: 1200px; height: 900px; overflow: hidden; }
  body {
    background: var(--backdrop);
    font-family: "Mulish", sans-serif;
    position: relative;
  }
  .card {
    position: absolute;
    top: 160px;
    width: 340px;
    height: 580px;
    border-radius: 22px;
    overflow: hidden;
  }
  .card-front { left: 190px; background: var(--purple); }
  .card-back { left: 670px; background: var(--white); }

  .brand { display: flex; flex-direction: column; align-items: center; }
  .brand-row { display: flex; align-items: center; gap: 12px; }
  .brand-mark { width: 22px; height: 22px; background: var(--red); }
  .brand-name { font-weight: 800; letter-spacing: 3px; }
  .brand-tagline { font-weight: 600; letter-spacing: 1.5px; }

  .card-front .brand { position: absolute; top: 230px; left: 0; right: 0; }
  .card-front .brand-name { color: var(--white); font-size: 44px; }
  .card-front .brand-tagline { color: var(--white); font-size: 15px; margin-top: 6px; }

  .card-back .brand { position: absolute; top: 62px; left: 0; right: 0; }
  .card-back .brand-mark { width: 16px; height: 16px; }
  .card-back .brand-name { color: var(--purple); font-size: 32px; }
  .card-back .brand-tagline { color: var(--purple); font-size: 11px; margin-top: 4px; }

  .holder { position: absolute; top: 170px; right: 34px; text-align: right; }
  .holder-name { color: var(--red); font-size: 17px; font-weight: 600; letter-spacing: 0.5px; }
  .holder-title {
    color: var(--ink); font-size: 13px; font-weight: 600;
    display: inline-block; padding: 2px 0 4px 40px;
    border-bottom: 2px solid var(--red);
  }

  .contact-accent {
    position: absolute; top: 262px; left: 26px; width: 320px; height: 230px;
    background: var(--red);
  }
  .contact-panel {
    position: absolute; top: 250px; left: 40px; right: 0; height: 230px;
    background: var(--purple);
    padding: 34px 14px 0 24px;
    display: flex; flex-direction: column; gap: 16px;
  }
  .contact-item { display: flex; align-items: center; gap: 14px; color: var(--white); font-size: 13px; line-height: 1.35; }
  .contact-icon {
    flex: none; width: 26px; height: 26px; border-radius: 5px;
    background: var(--white); display: flex; align-items: center; justify-content: center;
  }
  .contact-icon svg { width: 16px; height: 16px; }

  .coupon {
    position: absolute; bottom: 38px; left: 0; right: 0;
    text-align: center; color: var(--purple); font-size: 13px; font-weight: 600;
  }
</style>
</head>
<body>

<section class="card card-front">
  <div class="brand">
    <div class="brand-row">
      <span class="brand-mark"></span>
      <span class="brand-name">FORTIVAN</span>
    </div>
    <span class="brand-tagline">built for every workout</span>
  </div>
</section>

<section class="card card-back">
  <div class="brand">
    <div class="brand-row">
      <span class="brand-mark"></span>
      <span class="brand-name">FORTIVAN</span>
    </div>
    <span class="brand-tagline">built for every workout</span>
  </div>

  <div class="holder">
    <p class="holder-name">Lorena K. Vasquez</p>
    <p class="holder-title">CEO</p>
  </div>

  <div class="contact-accent"></div>
  <div class="contact-panel">
    <div class="contact-item">
      <span class="contact-icon">
        <svg viewBox="0 0 16 16"><path d="M4 1.5l2.3 3-1.4 1.6c.8 1.9 2.3 3.4 4.2 4.2l1.6-1.4 3 2.3-1.3 2.6C7 13.5 2.5 9 1.4 2.8z" fill="#e3222c"/></svg>
      </span>
      <span>614.275.3081</span>
    </div>
    <div class="contact-item">
      <span class="contact-icon">
        <svg viewBox="0 0 16 16" fill="none" stroke="#e3222c" stroke-width="2" stroke-linecap="round"><path d="M7 9.5L9.5 7"/><path d="M6 6.5L4 8.5a2.5 2.5 0 003.5 3.5L9.5 10"/><path d="M10 9.5l2-2A2.5 2.5 0 008.5 4L6.5 6"/></svg>
      </span>
      <span>LVasquez@Fortivanco.example</span>
    </div>
    <div class="contact-item">
      <span class="contact-icon">
        <svg viewBox="0 0 16 16" fill="none" stroke="#e3222c" stroke-width="1.6"><circle cx="8" cy="8" r="6.2"/><ellipse cx="8" cy="8" rx="2.6" ry="6.2"/><path d="M1.8 8h12.4"/></svg>
      </span>
      <span>www.fortivanco.example</span>
    </div>
    <div class="contact-item">
      <span class="contact-icon">
        <svg viewBox="0 0 16 16"><path d="M8 1a5 5 0 00-5 5c0 3.8 5 9 5 9s5-5.2 5-9a5 5 0 00-5-5z" fill="#e3222c"/><circle cx="8" cy="6" r="1.8" fill="#fff"/></svg>
      </span>
      <span>P.O. Box 48317<br>Alderton, Ohio 22417</span>
    </div>
  </div>

  <p class="coupon">Sign up on our website for a coupon code</p>
</section>

</body>
</html>
```